Small Box Design - For launch into retail market

We need artwork for small boxes that we are going to be using for the retail market. I will upload the type of box we are going to be using. The example we are uploading is of a different company that sells the same products. We would like our Logo on the box as as our web address (www.brandellgroup-ltd.com). The rest is up to you. Please contact with any questions.

Target Market(s)

Distributors, Retailers of Fasteners

Industry/Entity Type

Manufacture

Colors
0355a3
3176b5
fbee3f
fbf289

Requirements
Must have
• Our logo, our web address www.brandellgroup-ltd.com
• Somewhere on the box Washers . Stampings . Assemblies . Bearings (most likely below our logo somewhere)
Nice to have
• Blue is our corporate colour, but it's not essential. You can suggest any colours and we will consider.

```html
<!DOCTYPE html>
<html lang="en">
<head>
<meta charset="utf-8">
<title>Brandell Group – Retail Box Dieline</title>
<link href="https://fonts.googleapis.com/css2?family=Montserrat:wght@500;600;700;800&display=swap" rel="stylesheet">
<style>
  :root{
    --flap-blue:#6fafd9;
    --navy:#0b2f66;
    --corporate:#0355a3;
    --mid-blue:#3176b5;
    --lid-dark:#0c3f7e;
    --lid-light:#1d66a8;
    --gold:#c9a45c;
    --tile-pale:#eaf3fb;
    --white:#ffffff;
  }
  *{box-sizing:border-box;margin:0;padding:0}
  html,body{width:1200px;height:800px;overflow:hidden;background:var(--white)}
  body{position:relative;font-family:"Montserrat",sans-serif}
  .dieline{position:absolute;left:0;top:0}
  .panel{position:absolute;overflow:hidden}
  .pattern{position:absolute;inset:0;
    background:
      radial-gradient(ellipse at 30% 70%, rgba(3,85,163,.55), transparent 60%),
      radial-gradient(ellipse at 80% 20%, rgba(49,118,181,.45), transparent 55%),
      linear-gradient(135deg,var(--tile-pale),#b9d6ef 55%,var(--white));}
  .panel-content{position:absolute;inset:0;display:flex;flex-direction:column;align-items:center;justify-content:center;text-align:center}
  .flipped{transform:rotate(180deg)}
  .brand-name{font-weight:700;color:var(--navy);letter-spacing:.3px;line-height:1;white-space:nowrap}
  .product-line{display:inline-block;background:var(--navy);color:var(--white);font-weight:700;font-size:5.5px;padding:2px 6px;border-radius:2px;margin-top:4px;white-space:nowrap}
  .web{color:var(--navy);font-size:7px;font-weight:500;margin-top:3px;white-space:nowrap}
  .quote-band{position:absolute;left:0;right:0;background:var(--navy);color:var(--white);font-weight:700;font-size:8px;line-height:1.2;padding:4px 8px 4px 22px;text-align:left;white-space:nowrap}
  .quote-band .mark{position:absolute;left:7px;top:2px;font-size:16px;line-height:1}
  .lid{background:radial-gradient(ellipse at 75% 80%, var(--lid-light), var(--lid-dark) 70%)}
  .lid .brand-name{color:var(--white);font-size:24px}
  .lid .product-line{background:none;font-size:6.5px;margin-top:8px}
  .lid .web{color:var(--gold);font-size:7.5px;letter-spacing:.5px}
  .lid-square{position:absolute;left:12px;top:14px;width:14px;height:14px;background:var(--white)}
  .carton-code{position:absolute;left:244px;top:532px;transform:rotate(180deg);font-size:12px;font-weight:800;color:var(--navy);text-align:center;line-height:1}
  .carton-code small{display:block;font-size:4px;font-weight:600}
  .brand-lockup{position:absolute;left:664px;top:120px;display:flex;align-items:center;gap:16px}
  .lockup-circle{width:70px;height:70px;border-radius:50%;background:var(--gold);flex:none}
  .lockup-name{font-size:42px;font-weight:700;color:var(--corporate);line-height:1;white-space:nowrap}
</style>
</head>
<body>

<svg class="dieline" width="1200" height="800" viewBox="0 0 1200 800" aria-hidden="true">
  <g fill="var(--flap-blue)">
    <path d="M180 70 H392 C450 70 480 100 480 150 V180 H92 V150 C92 100 122 70 180 70 Z"/>
    <path d="M26 240 H98 L106 232 H150 L158 240 H172 V344 H26 Z"/>
    <path d="M398 240 H452 L460 232 H504 L512 240 H546 V344 H398 Z"/>
    <rect x="18" y="462" width="536" height="60"/>
    <rect x="180" y="462" width="212" height="162"/>
    <rect x="18" y="624" width="160" height="118"/>
    <rect x="394" y="624" width="160" height="118"/>
  </g>
  <g class="recycle-icon" fill="none" stroke="var(--navy)" stroke-width="4" stroke-linejoin="round">
    <path d="M303 554 L288 528 H318 Z"/>
  </g>
</svg>

<!-- tuck flap -->
<section class="panel" style="left:180px;top:68px;width:212px;height:112px">
  <div class="panel-content flipped">
    <div class="pattern" role="img" aria-label="Soft blue mosaic tile background"></div>
    <div style="position:relative;margin-top:-30px">
      <div class="brand-name" style="font-size:18px">Brandell Group</div>
      <div class="product-line">Washers · Stampings · Assemblies · Bearings</div>
    </div>
    <div class="quote-band" style="bottom:6px"><span class="mark">“</span>trusted partner for the production<br>and supply of washers and pressed<br>components for trade and industry ”</div>
  </div>
</section>

<!-- lid -->
<section class="panel lid" style="left:180px;top:184px;width:212px;height:160px">
  <div class="lid-square"></div>
  <div class="panel-content">
    <div class="brand-name">Brandell Group</div>
    <div class="product-line">Washers · Stampings · Assemblies · Bearings</div>
    <div class="web">www.brandellgroup-ltd.com</div>
  </div>
</section>

<!-- front row -->
<section class="panel" style="left:18px;top:344px;width:160px;height:118px">
  <div class="pattern" role="img" aria-label="Soft blue mosaic tile background"></div>
  <div class="panel-content">
    <div class="brand-name" style="font-size:16px">Brandell Group</div>
    <div class="product-line" style="font-size:4.5px">Washers · Stampings · Assemblies · Bearings</div>
    <div class="web" style="font-size:5.5px">www.brandellgroup-ltd.com</div>
  </div>
</section>
<section class="panel" style="left:182px;top:344px;width:210px;height:118px">
  <div class="pattern" role="img" aria-label="Soft blue mosaic tile background"></div>
  <div class="panel-content">
    <div class="brand-name" style="font-size:21px">Brandell Group</div>
    <div class="product-line">Washers · Stampings · Assemblies · Bearings</div>
    <div class="web">www.brandellgroup-ltd.com</div>
  </div>
</section>
<section class="panel" style="left:394px;top:344px;width:160px;height:118px">
  <div class="pattern" role="img" aria-label="Soft blue mosaic tile background"></div>
  <div class="panel-content">
    <div class="brand-name" style="font-size:16px">Brandell Group</div>
    <div class="product-line" style="font-size:4.5px">Washers · Stampings · Assemblies · Bearings</div>
    <div class="web" style="font-size:5.5px">www.brandellgroup-ltd.com</div>
  </div>
</section>

<div class="carton-code">4<small>SIZE</small></div>

<!-- back panel -->
<section class="panel" style="left:180px;top:624px;width:212px;height:118px">
  <div class="panel-content flipped">
    <div class="pattern" role="img" aria-label="Soft blue mosaic tile background"></div>
    <div style="position:relative;margin-top:-34px">
      <div class="brand-name" style="font-size:18px">Brandell Group</div>
      <div class="product-line">Washers · Stampings · Assemblies · Bearings</div>
    </div>
    <div class="quote-band" style="bottom:8px"><span class="mark">“</span>trusted partner for the production<br>and supply of washers and pressed<br>components for trade and industry ”</div>
  </div>
</section>

<!-- brand lockup -->
<div class="brand-lockup">
  <div class="lockup-circle"></div>
  <div class="lockup-name">Brandell Group</div>
</div>

</body>
</html>
```